Pellory T's Menu boxes

HI

This project if for the design of some illuminated menu boxes for inside a shop.

We sell Ice Cream, Milk shakes, Smoothies and some cakes.

The shop is mainly pink in colour, i have had some posters done for the windows and would like the menus to maintain the feel of the posters. i have 8 menu boards but will probably onlu use 4.

i will attach a few of the posters so you can see the feel im looking for and the menu should have:
a section for ice creams
a section for milk shakes
a section for smoothies
a section for coffees and teas
and a section for juices
and a section for desserts.

Regards
Updates

Hi

I have now attached the logos source file

Many thanks

Reason: Hi for some reason only one designer has responded therefore i am extending the deadline thanks

Hi All

I have now increased the budget on the project

Many Thanks

```html
<!DOCTYPE html>
<html lang="en">
<head>
<meta charset="utf-8">
<title>Pellory T's – Ice Cream Menu Board</title>
<link href="https://fonts.googleapis.com/css2?family=Sniglet:wght@400;800&family=Comic+Neue:wght@700&display=swap" rel="stylesheet">
<style>
  :root {
    --frame-purple: #8f2a8e;
    --shadow-purple: #8b2e8b;
    --hot-pink: #e5128c;
    --menu-yellow: #fde600;
    --addon-purple: #8a3a8a;
    --white: #ffffff;
  }
  * { margin: 0; padding: 0; box-sizing: border-box; }
  html, body { width: 1200px; height: 844px; overflow: hidden; background: var(--white); }
  .menu-board { position: relative; width: 1200px; height: 844px; overflow: hidden; }
  .board-frame { position: absolute; inset: 0; }

  .cone-photo {
    position: absolute; left: 140px; top: 95px; width: 290px; height: 232px;
    border-radius: 40px 40px 110px 110px;
    background: linear-gradient(100deg, #8d6bb8 0%, #f27fb8 45%, #9a6347 75%, #e3b777 100%);
  }

  .brand-name {
    position: absolute; left: 603px; top: 92px; transform: translateX(-50%);
    font-family: "Sniglet", system-ui, sans-serif; font-weight: 800; font-size: 50px;
    line-height: 1; color: var(--hot-pink); white-space: nowrap;
  }

  .bubble {
    position: absolute; z-index: 2; font-family: "Sniglet", system-ui, sans-serif; font-weight: 800;
    color: var(--hot-pink); white-space: nowrap; line-height: 1;
    -webkit-text-stroke: 2px var(--white); paint-order: stroke fill;
    text-shadow: 0 0 1px var(--white), 2px 2px 0 var(--frame-purple), -2px -2px 0 var(--frame-purple),
                 2px -2px 0 var(--frame-purple), -2px 2px 0 var(--frame-purple), 3px 3px 0 var(--frame-purple);
  }
  .centered { transform: translateX(-50%); }
  .group-title { font-size: 42px; top: 210px; }
  .size-label { font-size: 42px; top: 283px; }
  .price { font-size: 38px; top: 357px; }
  .category-title { font-size: 54px; left: 15px; top: 342px; }

  .flavour-panel {
    position: absolute; left: 10px; top: 466px; width: 1080px; height: 214px;
    background: var(--menu-yellow); border-radius: 0 14px 14px 0;
    box-shadow: 8px 8px 0 var(--shadow-purple);
  }
  .flavour-list {
    position: absolute; top: 473px; list-style: none;
    font-family: "Comic Neue", "Comic Sans MS", cursive; font-weight: 700; font-size: 35px;
    letter-spacing: 0.6px; color: var(--hot-pink); line-height: 48px; white-space: nowrap;
  }
  .col-1 { left: 18px; } .col-2 { left: 414px; } .col-3 { left: 810px; }

  .addon {
    position: absolute; top: 712px; font-family: "Comic Neue", "Comic Sans MS", cursive;
    font-weight: 700; font-size: 36px; letter-spacing: 1.4px; color: var(--addon-purple); white-space: nowrap;
  }
</style>
</head>
<body>
<main class="menu-board">
  <svg class="board-frame" width="1200" height="844" viewBox="0 0 1200 844" aria-hidden="true">
    <path d="M6,838 L6,290 C20,120 300,10 600,8 C900,10 1180,120 1194,290 L1194,838 Z"
          fill="none" stroke="var(--frame-purple)" stroke-width="9"/>
    <line x1="0" y1="834" x2="1200" y2="834" stroke="var(--frame-purple)" stroke-width="9"/>
  </svg>

  <div class="cone-photo" role="img" aria-label="Photo of three ice cream cones: purple, pink and chocolate scoops"></div>

  <h1 class="brand-name">Pellory T's</h1>

  <span class="bubble group-title centered" style="left:557px">CONES</span>
  <span class="bubble group-title centered" style="left:955px">CUP</span>

  <span class="bubble size-label centered" style="left:448px">S</span>
  <span class="bubble size-label centered" style="left:557px">M</span>
  <span class="bubble size-label centered" style="left:667px">L</span>
  <span class="bubble size-label centered" style="left:846px">S</span>
  <span class="bubble size-label centered" style="left:955px">M</span>
  <span class="bubble size-label centered" style="left:1062px">L</span>

  <h2 class="bubble category-title">Ice Cream</h2>

  <span class="bubble price centered" style="left:448px">1.95</span>
  <span class="bubble price centered" style="left:557px">2.55</span>
  <span class="bubble price centered" style="left:660px">2.95</span>
  <span class="bubble price centered" style="left:845px">2.25</span>
  <span class="bubble price centered" style="left:955px">2.85</span>
  <span class="bubble price centered" style="left:1060px">3.35</span>

  <div class="flavour-panel"></div>
  <ul class="flavour-list col-1">
    <li>Rum Raisin</li><li>Tiger</li><li>Strawberry</li><li>Lychee Passion Fruit</li>
  </ul>
  <ul class="flavour-list col-2">
    <li>Chocolate Mint</li><li>Peanut Butter Ripple</li><li>Cherry Cheesecake</li><li>Apple Pear</li>
  </ul>
  <ul class="flavour-list col-3">
    <li>Bubblegum</li><li>Vanilla</li><li>Mocha Java</li><li>Guava Peach</li>
  </ul>

  <span class="addon" style="left:20px">Add Wafer Cone</span>
  <span class="addon" style="left:380px">.55</span>
  <span class="addon" style="left:605px">Add Topping</span>
  <span class="addon" style="left:880px">.35each</span>
</main>
</body>
</html>
```